Bref créative
Business Card for financial advisor
RVT Service Providers
Simple
Irina Lebedinskaya
Director
42 Marlow Yard
London
SW9 3QT
irina.lebedinskaya@rvtsupport.example

```html
<!DOCTYPE html>
<html lang="en">
<head>
<meta charset="utf-8">
<title>RVT Service Providers – Business Card</title>
<link rel="stylesheet" href="https://fonts.googleapis.com/css2?family=Open+Sans:wght@400;700&display=swap">
<style>
  :root {
    --page-bg: #e9e6e2;
    --card-white: #ffffff;
    --band-black: #141414;
    --brand-red: #d0101a;
    --brand-red-deep: #a9080f;
    --ink: #1a1a1a;
    --divider: #9a9a9a;
    --text-light: #ffffff;
  }
  * { box-sizing: border-box; margin: 0; padding: 0; }
  html, body {
    width: 1200px;
    height: 878px;
    overflow: hidden;
    background: var(--page-bg);
    font-family: "Open Sans", Arial, sans-serif;
  }
  .canvas {
    position: relative;
    width: 1200px;
    height: 878px;
  }
  .card {
    position: absolute;
    left: 100px;
    top: 153px;
    width: 1000px;
    height: 572px;
    border-radius: 28px;
    overflow: hidden;
    background: var(--card-white);
    box-shadow: 0 14px 40px rgba(0,0,0,0.18);
  }
  .card__top {
    position: absolute;
    left: 0; top: 0;
    width: 100%;
    height: 255px;
    background: linear-gradient(180deg, #ffffff 0%, #f3f3f3 100%);
  }
  .brand {
    position: absolute;
    left: 0; right: 0;
    top: 100px;
    text-align: center;
  }
  .brand__name {
    font-weight: 700;
    font-size: 46px;
    letter-spacing: -1px;
    color: var(--ink);
    line-height: 1;
  }
  .card__band {
    position: absolute;
    left: 0; top: 255px;
    width: 100%;
    height: 76px;
    background: linear-gradient(180deg, #2a2a2a 0%, var(--band-black) 100%);
    display: flex;
    align-items: center;
    padding-left: 232px;
  }
  .person {
    font-size: 26px;
    font-weight: 400;
    color: var(--text-light);
    letter-spacing: 0.3px;
  }
  .person__divider { color: var(--divider); margin: 0 10px; }
  .person__role { color: var(--brand-red); }
  .card__base {
    position: absolute;
    left: 0; top: 339px;
    width: 100%;
    height: 233px;
    background: linear-gradient(180deg, var(--brand-red) 0%, var(--brand-red-deep) 100%);
    color: var(--text-light);
  }
  .address {
    position: absolute;
    right: 62px;
    top: 108px;
    font-size: 18px;
    font-weight: 400;
  }
  .contacts {
    position: absolute;
    right: 62px;
    top: 150px;
    font-size: 17px;
    white-space: nowrap;
  }
  .contacts__label { font-weight: 700; }
  .contacts__sep { margin: 0 8px; }
</style>
</head>
<body>
<main class="canvas">
  <article class="card">
    <header class="card__top">
      <div class="brand">
        <span class="brand__name">RVT Service Providers</span>
      </div>
    </header>

    <section class="card__band">
      <p class="person">
        <span class="person__name">Irina Lebedinskaya</span><span class="person__divider">|</span><span class="person__role">Director</span>
      </p>
    </section>

    <footer class="card__base">
      <p class="address">42 Marlow Yard London SW9 3QT</p>
      <p class="contacts">
        <span class="contacts__label">Phone:</span> +44 (0) 207 555 0148<span class="contacts__sep">|</span><span class="contacts__label">Cell:</span> +44 (0) 770 555 0193<span class="contacts__sep">|</span><span class="contacts__label">Email:</span> irina.lebedinskaya@rvtsupport.example
      </p>
    </footer>
  </article>
</main>
</body>
</html>
```